I Need a New Design For Existing Wordpress Site

My website is www.sundaystrummer.net. The purpose is to provide free guitar lessons. Each blog post is a new video lesson embedded from ClipHarbor. The site is also an avenue to sell my ebook.

I need a Wordpress design that is appealing and professional. It should make the user feel as if the site is legitimate and trustworthy. I like the color schemes that use blues, grey,s and white matching my logo.

Examples of website designs I like:
www.riffolio.com
www.tealmistworks.com
www.quietearningsdesk.com

Target Market(s)

15-35 year old males. Rock n roll, country, and pop music

Industry/Entity Type

ClipHarbor

Font styles to use
Sans Serif

Colors
0255a3
0792cd
ffffff
333333

Requirements
Must have
• Modern professional look

```html
<!DOCTYPE html>
<html lang="en">
<head>
<meta charset="utf-8">
<title>Sunday Strummer – Blog</title>
<link rel="stylesheet" href="https://fonts.googleapis.com/css2?family=Lato:wght@400;700&family=Lora:wght@400&family=Playfair+Display:wght@400;700&display=swap">
<style>
:root{
  --page:#f2f2f2;
  --card:#ffffff;
  --ink:#333333;
  --muted:#8a8a8a;
  --line:#e6e6e6;
  --brand-dark:#0255a3;
  --brand:#0792cd;
  --accent:#f5c400;
  --media-dark:#3e3e3e;
  --player-red:#e8431f;
}
*{margin:0;padding:0;box-sizing:border-box}
html,body{width:1200px;height:1000px;overflow:hidden;background:var(--page)}
body{position:relative;font-family:"Lato",sans-serif;color:var(--ink)}
.abs{position:absolute}

/* Post blocks */
.post-tag{position:absolute;display:flex;height:22px;font:400 11px "Lato",sans-serif;color:#fff}
.post-tag .label{background:var(--brand-dark);padding:0 8px 0 5px;line-height:24px}
.post-tag .count{background:var(--brand);width:19px;text-align:center;font-size:15px;line-height:22px}
.post-head{position:absolute;left:239px;width:478px;height:90px;background:var(--card)}
.post-icon{position:absolute;left:-20px;top:13px;width:39px;height:39px;border-radius:50%;background:var(--accent);border:3px solid #fff;box-shadow:0 0 0 1px #f0e3a8;display:flex;align-items:center;justify-content:center}
.post-title{position:absolute;left:35px;top:7px;width:420px;font:400 20.5px/26px "Lora",serif;color:var(--ink)}
.post-meta{position:absolute;left:35px;top:63px;display:flex;gap:17px;font:400 7.5px "Lato",sans-serif;text-transform:uppercase;color:var(--muted);letter-spacing:.2px}
.post-meta span{display:flex;align-items:center;gap:6px}
.post-body{position:absolute;left:239px;width:478px;background:var(--card);box-shadow:0 2px 0 #e9e9e9}
.photo{position:absolute;display:flex;align-items:center;justify-content:center}
.play{width:26px;height:19px;border-radius:4px;background:rgba(20,20,20,.8);display:flex;align-items:center;justify-content:center}
.excerpt{position:absolute;left:19px;top:515px;width:420px;font:400 8.6px/15px "Lato",sans-serif;color:#666}
.post-foot{position:absolute;left:0;top:574px;width:478px;height:33px;border-top:1px solid var(--line);display:flex;align-items:center}
.share{display:flex;gap:15px;margin-left:26px}
.share i{display:block;width:7px;height:7px;border-radius:50%;background:#444}
.read-more{position:absolute;right:0;top:0;width:37px;height:33px;border-left:1px solid var(--line);display:flex;align-items:center;justify-content:center}

/* Audio embed */
.player{position:absolute;left:3px;top:32px;width:472px;height:90px;display:flex}
.player-badge{width:104px;background:#2a2a2a;display:flex;align-items:center;justify-content:center;gap:5px;color:#fff;font:700 13px "Lato",sans-serif}
.player-badge i{width:18px;height:18px;border-radius:50%;background:#fff;display:block}
.player-main{flex:1;background:#f6f6f6;position:relative}
.player-btn{position:absolute;left:4px;top:4px;width:26px;height:26px;border-radius:50%;background:var(--player-red)}
.player-artist{position:absolute;left:36px;top:5px;font:400 8px "Lato",sans-serif;color:#999}
.player-track{position:absolute;left:36px;top:17px;font:400 9px "Lato",sans-serif;color:#333}
.wave{position:absolute;left:4px;top:42px;width:356px;height:40px;display:flex;align-items:flex-end;gap:1px}
.wave b{flex:1;background:#555}

/* Sidebar */
.sidebar{position:absolute;left:735px;top:0;width:230px;height:1000px;background:var(--card);border-left:1px solid var(--line);border-right:1px solid var(--line)}
.widget-title{position:absolute;display:flex;align-items:center;gap:10px;font:400 12px "Playfair Display",serif;color:var(--ink)}
.widget-title::before{content:"";display:block;width:16px;height:4px;border-top:1px solid var(--line);border-bottom:1px solid var(--line)}
.cat-list{position:absolute;left:26px;top:42px;width:178px;list-style:none;border-top:1px solid var(--line)}
.cat-list li{height:32px;border-bottom:1px solid var(--line);display:flex;align-items:center;justify-content:space-between;font:400 8.5px "Lato",sans-serif}
.cat-list em{font-style:normal;width:19px;height:19px;border:1px solid var(--line);border-radius:50%;font-size:7px;display:flex;align-items:center;justify-content:center;color:#666}
.tabs{position:absolute;left:13px;top:165px;display:flex;gap:4px}
.tabs span{height:36px;border:1px solid var(--line);display:flex;align-items:center;justify-content:center;font:400 7px "Playfair Display",serif;text-transform:uppercase;color:#aaa;letter-spacing:.3px}
.tabs .active{border-top:2px solid var(--accent);color:var(--ink)}
.side-title{position:absolute;left:26px;width:185px;font:400 10.5px/15px "Playfair Display",serif;color:var(--ink)}
.side-date{position:absolute;left:26px;display:flex;gap:7px;align-items:center;font:400 7.5px "Lato",sans-serif;color:#777}
.vid-item{position:absolute;left:29px;display:flex;gap:8px}
.vid-thumb{width:49px;height:44px;background:linear-gradient(135deg,#3a3030,#a58f84 55%,#2a2424)}
.vid-item p{font:400 8px/11px "Lato",sans-serif;color:var(--ink);width:100px}
.vid-item small{display:block;margin-top:5px;font-size:6.5px;color:#777;text-transform:uppercase}
</style>
</head>
<body>

<!-- Post 1 -->
<div class="post-tag" style="left:239px;top:5px"><span class="label">Lesson</span><span class="count">2</span></div>
<article class="post-head" style="top:27px">
  <div class="post-icon"><svg width="14" height="14" viewBox="0 0 14 14"><path d="M5 2l7-1.5v8.5a2 2 0 1 1-1.4-1.9V3.6L6.4 4.5V11a2 2 0 1 1-1.4-1.9z" fill="#fff"/></svg></div>
  <h2 class="post-title">Carry Me Home Beginner Guitar Lesson – Ardell Finch – Easy Chords</h2>
  <div class="post-meta">
    <span><svg width="8" height="8"><rect x=".5" y="1.5" width="7" height="6" fill="none" stroke="#999"/></svg>5 Mar 2015</span>
    <span><svg width="9" height="8"><ellipse cx="4.5" cy="3.5" rx="4.5" ry="3.2" fill="#999"/></svg>0 Comments</span>
    <span><svg width="8" height="8"><circle cx="4" cy="2.3" r="2.2" fill="#999"/><path d="M0 8a4 3.5 0 0 1 8 0z" fill="#999"/></svg>Admin</span>
    <span><svg width="9" height="8"><path d="M4.5 8L.5 3.8A2.2 2.2 0 0 1 4.5 1.5 2.2 2.2 0 0 1 8.5 3.8z" fill="#999"/></svg>1 Likes</span>
  </div>
</article>
<article class="post-body" style="top:122px;height:607px">
  <div class="photo" role="img" aria-label="Instructor seated with acoustic guitar against a dark backdrop" style="left:13px;top:27px;width:452px;height:306px;background:linear-gradient(160deg,#2e2627,#5d5258 45%,#c9a47d 70%,#6c7b91)"></div>
  <div class="photo" role="img" aria-label="Close-up of hand fretting a chord on an acoustic guitar neck" style="left:13px;top:339px;width:224px;height:152px;background:linear-gradient(120deg,#c9a3a8,#e8d7d6 35%,#262222 65%,#8a6e57)"><div class="play"><svg width="8" height="9"><path d="M0 0l8 4.5L0 9z" fill="#fff"/></svg></div></div>
  <div class="photo" role="img" aria-label="Close-up of chord shape on guitar fretboard" style="left:243px;top:339px;width:222px;height:152px;background:linear-gradient(120deg,#6f86b8,#a9b9d6 35%,#1e1c1c 65%,#9a7f66)"><div class="play"><svg width="8" height="9"><path d="M0 0l8 4.5L0 9z" fill="#fff"/></svg></div></div>
  <p class="excerpt">Cras sit amet dui ac lectus molestie porttitor. Aenean sagittis imperdiet massa. Nam est lacus, consequat vita eil semper tristique, temp us in magna. Nullam sit amet metus eget dolor semper laoreet ...</p>
  <div class="post-foot">
    <div class="share"><i></i><i></i><i></i><i></i><i></i><i></i></div>
    <div class="read-more"><svg width="11" height="6"><path d="M0 3h9M7 .5L10 3 7 5.5" fill="none" stroke="#333" stroke-width="1.2"/></svg></div>
  </div>
</article>

<!-- Post 2 -->
<div class="post-tag" style="left:239px;top:765px"><span class="label">Lesson</span><span class="count">2</span></div>
<article class="post-head" style="top:785px">
  <div class="post-icon"><svg width="14" height="14" viewBox="0 0 14 14"><path d="M5 2l7-1.5v8.5a2 2 0 1 1-1.4-1.9V3.6L6.4 4.5V11a2 2 0 1 1-1.4-1.9z" fill="#fff"/></svg></div>
  <h2 class="post-title" style="left:37px">Worn Boots Video Guitar Lesson – Dale Harmon Jr – How to Play Chords</h2>
  <div class="post-meta">
    <span><svg width="8" height="8"><rect x=".5" y="1.5" width="7" height="6" fill="none" stroke="#999"/></svg>4 Mar 2015</span>
    <span><svg width="9" height="8"><ellipse cx="4.5" cy="3.5" rx="4.5" ry="3.2" fill="#999"/></svg>0 Comments</span>
    <span><svg width="8" height="8"><circle cx="4" cy="2.3" r="2.2" fill="#999"/><path d="M0 8a4 3.5 0 0 1 8 0z" fill="#999"/></svg>Admin</span>
    <span><svg width="9" height="8"><path d="M4.5 8L.5 3.8A2.2 2.2 0 0 1 4.5 1.5 2.2 2.2 0 0 1 8.5 3.8z" fill="#999"/></svg>0 Likes</span>
  </div>
</article>
<article class="post-body" style="top:880px;height:130px">
  <div class="player">
    <div class="player-badge"><i></i>ClipHarbor</div>
    <div class="player-main">
      <div class="player-btn"></div>
      <div class="player-artist">Vapor Lines</div>
      <div class="player-track">Vapor Lines - Drift (feat. Nolan Crest)</div>
      <div class="wave">
        <b style="height:55%"></b><b style="height:70%"></b><b style="height:62%"></b><b style="height:80%"></b><b style="height:66%"></b><b style="height:74%"></b><b style="height:58%"></b><b style="height:85%"></b><b style="height:72%"></b><b style="height:64%"></b><b style="height:78%"></b><b style="height:60%"></b><b style="height:82%"></b><b style="height:69%"></b><b style="height:75%"></b><b style="height:57%"></b><b style="height:88%"></b><b style="height:71%"></b><b style="height:63%"></b><b style="height:79%"></b><b style="height:67%"></b><b style="height:84%"></b><b style="height:59%"></b><b style="height:76%"></b><b style="height:70%"></b><b style="height:86%"></b><b style="height:61%"></b><b style="height:73%"></b><b style="height:68%"></b><b style="height:81%"></b><b style="height:65%"></b><b style="height:77%"></b><b style="height:58%"></b><b style="height:83%"></b><b style="height:72%"></b><b style="height:66%"></b><b style="height:79%"></b><b style="height:62%"></b><b style="height:74%"></b><b style="height:60%"></b>
      </div>
    </div>
  </div>
</article>

<!-- Sidebar -->
<aside class="sidebar">
  <h3 class="widget-title" style="left:0;top:5px">Recent Posts</h3>
  <ul class="cat-list">
    <li>Guitar Lesson<em>4</em></li>
    <li>Music<em>4</em></li>
    <li>Uncategorized<em>1</em></li>
  </ul>
  <div class="tabs">
    <span class="active" style="width:60px">Posts</span>
    <span style="width:79px">Comments</span>
    <span style="width:55px">Tags</span>
  </div>

  <div class="abs" role="img" aria-label="Promotional banner for online guitar lessons at www.sundaystrummer.net with a click here to get started button" style="left:26px;top:234px;width:179px;height:122px;background:linear-gradient(180deg,#7a1a14,#3a3a3a 40%,#555 70%,#1c1c1c)"></div>
  <h4 class="side-title" style="top:375px">Carry Me Home Beginner Guitar Ardell Finch – Easy Chords</h4>
  <div class="side-date" style="top:419px"><svg width="8" height="8"><rect x=".5" y="1.5" width="7" height="6" fill="none" stroke="#999"/></svg>6 March 2015</div>

  <div class="abs" role="img" aria-label="Guitarist playing acoustic guitar" style="left:26px;top:442px;width:179px;height:64px;background:linear-gradient(120deg,#2a2424,#c9a47d 50%,#6c7b91)"></div>
  <div class="abs" role="img" aria-label="Chord close-up" style="left:26px;top:509px;width:87px;height:58px;background:linear-gradient(120deg,#c9a3a8,#262222 60%,#8a6e57)"></div>
  <div class="abs" role="img" aria-label="Chord close-up" style="left:116px;top:509px;width:89px;height:58px;background:linear-gradient(120deg,#6f86b8,#1e1c1c 60%,#9a7f66)"></div>
  <h4 class="side-title" style="top:584px;left:31px">Worn Boots Video Guitar Lesson – Jr – How to Play Chords</h4>
  <div class="side-date" style="top:629px"><svg width="8" height="8"><rect x=".5" y="1.5" width="7" height="6" fill="none" stroke="#999"/></svg>5 March 2015</div>

  <div class="abs" style="left:26px;top:654px;width:179px;height:95px;background:var(--media-dark);display:flex;align-items:center;justify-content:center"><svg width="9" height="9" viewBox="0 0 14 14"><path d="M5 2l7-1.5v8.5a2 2 0 1 1-1.4-1.9V3.6L6.4 4.5V11a2 2 0 1 1-1.4-1.9z" fill="#fff"/></svg></div>
  <h4 class="side-title" style="top:764px;font-weight:700">Quisque tincidunt lectus vel</h4>
  <div class="side-date" style="top:790px"><svg width="8" height="8"><rect x=".5" y="1.5" width="7" height="6" fill="none" stroke="#999"/></svg>4 March 2015</div>

  <h3 class="widget-title" style="left:0;top:855px">ClipHarbor Video</h3>
  <div class="vid-item" style="top:893px"><div class="vid-thumb" role="img" aria-label="Guitar lesson video thumbnail"></div><p>Suspendise lerisque lorem ipsu dum dolor<small>Admin</small></p></div>
  <div class="vid-item" style="top:945px"><div class="vid-thumb" role="img" aria-label="Guitar lesson video thumbnail"></div><p>Vestibulum auctor lacinia nunc etiam ipsum<small>Admin</small></p></div>
  <div class="vid-item" style="top:997px"><div class="vid-thumb" role="img" aria-label="Guitar lesson video thumbnail"></div></div>
</aside>

</body>
</html>
```